Brightvantage.com tech company website

Current site is www.brightvantage.com. The site will tell you about our company.

Designs we like are:
http://megainfo.quellorix.com
www.trelvo.com
www.morvasket.com

Target Market(s)

B2B

Industry/Entity Type

It Company

Coding

Coded - Design and coding required

Number of Pages Required

5+ page

Requirements
Must have
• We want to entice without giving away too much info. We like graphics and colors. But website must look official and credible.

```html
<!DOCTYPE html>
<html lang="en">
<head>
<meta charset="utf-8">
<title>Brightvantage – IT Company</title>
<link rel="stylesheet" href="https://fonts.googleapis.com/css2?family=Open+Sans:wght@300;400;600;700&display=swap">
<style>
:root{
  --blue:#2a6ea6;
  --blue-dark:#1f5a8a;
  --ink:#333;
  --muted:#888;
  --line:#dcdcdc;
  --paper:#fff;
  --grey-bg:#f1f1f1;
  --footer:#1b1b1b;
  --footer-text:#9a9a9a;
}
*{box-sizing:border-box;margin:0;padding:0}
html,body{width:882px;height:1200px;overflow:hidden;background:var(--paper)}
body{font-family:"Open Sans",Arial,sans-serif;color:var(--ink);font-size:8px;line-height:1.5}
.page{width:882px;height:1200px;position:relative}

.site-header{height:52px;display:flex;align-items:center;justify-content:space-between;padding:0 70px 0 110px}
.brand{display:flex;align-items:center;gap:7px;font-weight:700;font-size:15px;color:var(--blue);letter-spacing:.5px}
.brand-mark{width:14px;height:14px;background:var(--blue);border-radius:50%}
.main-nav{display:flex;gap:20px;font-size:6.5px;text-transform:uppercase;color:#555;letter-spacing:.4px}

.hero{position:relative;height:228px}
.hero-photo{position:absolute;inset:0;background:linear-gradient(100deg,#c9d3dc 0%,#e8edf1 40%,#b8c4cf 75%,#8996a3 100%)}
.hero-copy{position:absolute;top:70px;width:100%;text-align:center;color:#fff}
.hero-title{font-size:15px;font-weight:600;letter-spacing:.6px;text-transform:uppercase;text-shadow:0 1px 3px rgba(0,0,0,.25)}
.hero-sub{font-size:10.5px;margin-top:4px}

.features{display:flex;justify-content:center;padding:28px 0 20px}
.feature{width:190px;text-align:center;padding:8px 24px;border-right:1px solid var(--line)}
.feature:last-child{border-right:none}
.feature h3{font-size:8px;font-weight:400;color:#555;line-height:1.3}
.feature svg{margin:8px 0}
.feature p{font-size:5.5px;color:var(--muted)}

.intro{text-align:center;padding:6px 0 18px}
.intro h2{font-size:13px;font-weight:400;color:var(--blue)}
.intro p{width:440px;margin:6px auto 0;font-size:5.5px;color:var(--muted)}
.intro .link{display:block;margin-top:10px;font-size:5.5px;color:#666}

.testimonial{background:var(--blue);height:168px;text-align:center;color:#fff;padding-top:22px}
.avatar{width:52px;height:52px;border-radius:50%;margin:0 auto;border:2px solid #fff;background:linear-gradient(160deg,#9aa7b3,#4b5967)}
.testimonial blockquote{width:360px;margin:14px auto 0;font-size:6px;line-height:1.6}
.testimonial cite{display:block;margin-top:14px;font-style:normal;font-size:6px}

.info{background:var(--grey-bg);height:290px;padding:28px 0 0}
.info-cols{display:flex;gap:50px;padding:0 110px}
.info-col{flex:1}
.info-col h4{font-size:8.5px;font-weight:400;color:#555;border-bottom:1px solid var(--line);padding-bottom:5px;margin-bottom:10px}
.info-col p{font-size:5.5px;color:var(--muted)}
.article{margin-bottom:10px}
.article .date{font-size:5.5px;color:#555;text-transform:uppercase}
.services li{list-style:none;font-size:5.5px;color:#666;text-transform:uppercase;margin-bottom:5px;padding-left:8px;position:relative}
.services li::before{content:"";position:absolute;left:0;top:3px;width:3px;height:3px;background:var(--blue);border-radius:50%}
.partners{display:flex;justify-content:center;gap:26px;margin-top:34px;align-items:center}
.partner{height:14px;background:#3a3a3a;border-radius:2px}

.site-footer{background:var(--footer);height:142px;color:var(--footer-text);padding:28px 110px 0;display:flex;gap:60px}
.foot-col{flex:1}
.foot-col h5{font-size:6.5px;color:#fff;font-weight:600;text-transform:uppercase;margin-bottom:8px}
.foot-col p,.foot-col li{font-size:5.5px;list-style:none;margin-bottom:3px}
.phone{display:flex;align-items:center;gap:5px;color:#fff;font-size:9px;margin:4px 0}
.social{display:flex;gap:6px;margin-bottom:8px}
.social span{width:14px;height:14px;border-radius:50%;background:#555}
</style>
</head>
<body>
<div class="page">
  <header class="site-header">
    <div class="brand"><span class="brand-mark"></span>BRIGHTVANTAGE</div>
    <nav class="main-nav"><span>Home</span><span>About Us</span><span>Business Domain</span><span>Solutions</span><span>Partners &amp; Alliances</span><span>Case Studies</span><span>Contact</span></nav>
  </header>

  <section class="hero">
    <div class="hero-photo" role="img" aria-label="Office desk with laptop and hands at work, soft grey-blue tones"></div>
    <div class="hero-copy">
      <h1 class="hero-title">Driving outstanding excellence in everything we do</h1>
      <p class="hero-sub">Our work is dedicated to the prosperity of our clients</p>
    </div>
  </section>

  <section class="features">
    <div class="feature">
      <h3>Client<br>Solutions</h3>
      <svg width="18" height="16" viewBox="0 0 18 16"><rect x="1" y="4" width="16" height="11" rx="1" fill="none" stroke="#2a6ea6" stroke-width="1.4"/><path d="M6 4V2h6v2" fill="none" stroke="#2a6ea6" stroke-width="1.4"/></svg>
      <p>Tailored services built around your goals, helping teams deliver results faster.</p>
    </div>
    <div class="feature">
      <h3>Core<br>Business</h3>
      <svg width="16" height="16" viewBox="0 0 16 16"><rect x="1.5" y="1.5" width="13" height="13" rx="1" fill="none" stroke="#2a6ea6" stroke-width="1.4"/><path d="M4 6h8M4 9h8M4 12h5" stroke="#2a6ea6" stroke-width="1.2"/></svg>
      <p>Reliable platforms and expert support that keep your operations running smoothly.</p>
    </div>
    <div class="feature">
      <h3>Big<br>Data Analytics</h3>
      <svg width="20" height="14" viewBox="0 0 20 14"><path d="M5 13a4 4 0 0 1 0-8 5 5 0 0 1 9.5 1A3.5 3.5 0 0 1 15 13z" fill="#2a6ea6"/></svg>
      <p>Turn raw information into clear insight with modern analytics and reporting tools.</p>
    </div>
  </section>

  <section class="intro">
    <h2>We will show you the way to success!</h2>
    <p>From strategy to delivery, our specialists combine deep technical skill with business sense. We help organisations modernise systems, protect data and grow with confidence in a changing market.</p>
    <span class="link">Contact Us</span>
  </section>

  <section class="testimonial">
    <div class="avatar" role="img" aria-label="Portrait photo of a client"></div>
    <blockquote>“Working with this team transformed how we manage our data. Their guidance was clear, their delivery on time, and the results exceeded every expectation we had.”</blockquote>
    <cite>Daniel Harrow</cite>
  </section>

  <section class="info">
    <div class="info-cols">
      <div class="info-col">
        <h4>About Us</h4>
        <p>Brightvantage is an IT company helping businesses plan, build and run technology that matters. Our consultants bring years of experience across software, infrastructure and analytics, working as a true partner to every client.</p>
      </div>
      <div class="info-col">
        <h4>Latest Articles</h4>
        <div class="article"><p class="date">12 May 2015</p><p>Five steps to a cleaner data strategy for growing teams.</p></div>
        <div class="article"><p class="date">28 Apr 2015</p><p>Why cloud migration starts with people, not servers.</p></div>
      </div>
      <div class="info-col">
        <h4>Services</h4>
        <ul class="services">
          <li>Cloud Technology</li><li>Managed Hosting</li><li>Consulting</li><li>Custom Software</li><li>Social Media Strategy</li><li>Big Data</li><li>Data Warehouse Systems</li>
        </ul>
      </div>
    </div>
    <div class="partners">
      <span class="partner" style="width:44px"></span><span class="partner" style="width:34px"></span><span class="partner" style="width:42px"></span><span class="partner" style="width:38px"></span><span class="partner" style="width:40px"></span><span class="partner" style="width:48px"></span><span class="partner" style="width:46px"></span><span class="partner" style="width:20px"></span>
    </div>
  </section>

  <footer class="site-footer">
    <div class="foot-col">
      <h5>Brightvantage</h5>
      <p>© 2015 Brightvantage.com</p>
    </div>
    <div class="foot-col">
      <h5>Online Support</h5>
      <div class="phone"><svg width="9" height="9" viewBox="0 0 10 10"><path d="M2 1l2 2-1 1.5a6 6 0 0 0 2.5 2.5L7 6l2 2-1.2 1.2C4.5 9 1 5.5.8 2.2z" fill="#fff"/></svg>+1 555 014 3920</div>
      <p>hello@brightvantage.com</p>
      <p>www.brightvantage.com</p>
    </div>
    <div class="foot-col">
      <h5>Site Link</h5>
      <div class="social"><span></span><span></span><span></span></div>
      <ul><li>Home</li><li>About Us</li><li>Solutions</li><li>Case Studies</li><li>Contact</li></ul>
    </div>
  </footer>
</div>
</body>
</html>
```